Computer consultant website

Vexlo Software is a newly started computer consulting company. It's a small one-man company that provides mostly Mobile applications but also websites in collaboration with designers. I'm running this company on the side of full time university studies.

I'm in need of a website which will function as:
Primarily - I'll direct potential clients to the page so they can read about the company, what i offer and past work.
Secondarily - Making my company visible through the web and maybe getting new clients.

The final design should look modern, clean and professional.

Pages that will be in the final website are (Note that it's not the exact titles as the page will not be in english):
* About
* Services (what Vexlo offers)
* Portfolio/work
* Short news (like PlanHives "News and press")
* Contact.

Inspiration
http://www.planhive.example/design/87836
http://www.brambleorb.example/
http://www.planhive.example/design/845881
http://www.planhive.example/design/1369424 - Lighter design, however a bit cluttered.

No programming code is needed delivered at all. Focus on designing rather then coding.

If you have any questions, do not hesitate to send me a message.

Target Market(s)

Non-technical entrepreneurs and small companies.

Industry/Entity Type

University

Requirements
Must have
• Must have my company logo (see attachment).

Must in any way use both colors from my logo.

A way to logically rearrange content to fit smaller screens. I will implement this design so that it can be pleasantly viewed on mobile devices. You don't necessarily need to provide exactly how the design would look on mobile devices.

I need the following types of page designs:
* Landing page
* Content page
* Portfolio/work (with accompanying inside/clicked) page

Landing/start page must in any way include at least the information:
* Shorter version of "About Vexlo"
* At least 1 most recent portfolio/work entry
* At least 1 most recent news entry
* Services that Vexlo offers.
Nice to have
Should not have
• Testimonials or newsletter.

```html
<!DOCTYPE html>
<html lang="en">
<head>
<meta charset="utf-8">
<title>Vexlo Software</title>
<link href="https://fonts.googleapis.com/css2?family=Open+Sans:wght@400;600;700&family=Audiowide&family=Dancing+Script&display=swap" rel="stylesheet">
<style>
:root{
  --blue:#2378ee;
  --blue-dark:#1a63cc;
  --green:#5aa515;
  --green-dark:#3f8a0c;
  --ink:#333;
  --muted:#8a8a8a;
  --dark:#262626;
  --darker:#1b1b1b;
  --page:#fafafa;
  --white:#fff;
}
*{margin:0;padding:0;box-sizing:border-box}
html,body{width:733px;height:1200px;overflow:hidden}
body{font-family:"Open Sans",Arial,sans-serif;color:var(--ink);background:var(--page);position:relative}
.abs{position:absolute}

/* header */
.site-header{position:absolute;left:0;top:0;width:733px;height:55px;background:var(--white)}
.brand{position:absolute;left:115px;top:12px;display:flex;align-items:center;gap:7px}
.brand-dot{width:30px;height:30px;border-radius:50%;background:var(--blue)}
.brand-name{font-size:27px;font-weight:600;color:#3a3a3a;letter-spacing:-.5px}
.main-nav{position:absolute;top:0;height:55px;display:flex;left:344px}
.nav-item{height:55px;display:flex;flex-direction:column;align-items:center;justify-content:flex-end;padding-bottom:9px;font-size:9px;color:#444;position:relative}
.nav-item svg{margin-bottom:6px}
.nav-item.active{background:var(--dark);color:#fff}
.nav-item.active::after{content:"";position:absolute;bottom:-1px;left:50%;margin-left:-5px;border:5px solid transparent;border-bottom-color:#fff}
.nav-item.contact{background:var(--green);color:#fff}

/* hero */
.hero{position:absolute;left:0;top:55px;width:733px;height:238px;background:linear-gradient(180deg,#2e2e2e,#222)}
.hero-title{position:absolute;left:115px;top:44px;font-family:"Audiowide",sans-serif;font-size:19px;font-weight:400;color:#fff;letter-spacing:1px;text-transform:uppercase;white-space:nowrap}
.hero-lead{position:absolute;left:115px;top:71px;font-size:16px;line-height:20px;color:#fff;width:235px}
.tag{position:absolute;top:125px;height:18px;width:119px;background:#fff;border-radius:9px;font-size:8.5px;color:var(--blue);display:flex;align-items:center;padding-left:6px;gap:5px}
.cta{position:absolute;left:114px;top:168px;width:167px;height:34px;background:linear-gradient(#6dbd22,#4a9410);color:#fff;font-size:19px;font-weight:600;display:flex;align-items:center;padding-left:13px;gap:8px}
.cta-dot{width:20px;height:20px;border-radius:50%;background:#fff;display:flex;align-items:center;justify-content:center}
.tablet{position:absolute;left:403px;top:5px;width:213px;height:206px;border-radius:12px;background:linear-gradient(135deg,#3a3a3a,#0d0d0d 45%,#4a5a6a);transform:rotate(-4deg)}
.slider-dots{position:absolute;top:217px;left:350px;display:flex;gap:4px}
.slider-dots span{width:7px;height:7px;border-radius:50%;background:#ddd}
.slider-dots span.on{background:var(--green)}

/* section titles */
.section-title{position:absolute;left:0;width:733px;text-align:center;font-size:19px;font-weight:400}
.section-title .hl{color:var(--blue)}
.intro{position:absolute;left:115px;width:503px;text-align:center;font-size:7.6px;line-height:11px;color:var(--muted)}

/* services */
.service{position:absolute;top:397px;width:115px;height:115px;border-radius:50%;background:#fff;box-shadow:0 2px 4px rgba(0,0,0,.18);text-align:center;padding-top:19px}
.service h3{font-size:11.5px;font-weight:400;margin-top:4px}
.service h3 .hl{color:var(--blue)}
.service p{font-size:6.4px;line-height:8.5px;color:var(--muted);width:80px;margin:5px auto 0}
.service.featured{background:radial-gradient(circle at 50% 40%,#2d86ff,#1658c4);color:#fff}
.service.featured p{color:#e8f0ff}

/* about */
.about{position:absolute;left:0;top:552px;width:733px;height:207px;background:var(--blue);color:#fff}
.about .section-title{top:22px;color:#fff}
.video{position:absolute;left:115px;top:56px;width:187px;height:116px;background:#d0d0d0;border:2px solid #eee;text-align:center;color:#777;font-size:8.5px;padding-top:32px}
.video-icon{width:30px;height:30px;border-radius:50%;background:#8d8d8d;margin:0 auto 8px;display:flex;align-items:center;justify-content:center}
.about-head{position:absolute;left:323px;top:55px;font-size:16px;font-weight:400}
.about-sub{position:absolute;left:326px;top:79px;font-size:7.6px;font-weight:700;color:#e9f0ff}
.about-text{position:absolute;left:325px;top:94px;width:290px;font-size:7px;line-height:10px}
.btn{position:absolute;height:17px;background:linear-gradient(#61b31a,#448d0e);color:#fff;font-size:8.5px;display:flex;align-items:center;justify-content:center;gap:5px;border-radius:2px}
.btn i{width:9px;height:9px;border-radius:50%;background:#fff;display:inline-block}

/* portfolio */
.work{position:absolute;top:851px;width:108px;text-align:center}
.work-thumb{width:108px;height:108px;border-radius:50%;border:3px solid #fff;box-shadow:0 1px 4px rgba(0,0,0,.25);display:flex;align-items:center;justify-content:center;color:#fff;font-size:14px}
.work h4{font-size:10px;font-weight:400;margin-top:5px}
.work p{font-size:6.4px;line-height:8.5px;color:var(--muted);width:80px;margin:1px auto 0}

/* footer */
.site-footer{position:absolute;left:0;top:1058px;width:733px;height:117px;background:var(--darker);color:#ccc}
.footer-h{position:absolute;top:17px;font-size:9.5px;font-weight:400;color:#fff}
.sitemap{position:absolute;left:115px;top:35px;list-style:none;font-size:6.5px;line-height:12.2px;color:#999}
.news-item{position:absolute;left:183px;width:145px;font-size:6.1px;line-height:7.6px;color:#aaa}
.news-item em{display:block;font-size:5.5px;color:#777}
.map{position:absolute;left:374px;top:18px;width:162px;height:80px;background:linear-gradient(135deg,#e8e4d8,#d6e2c8 60%,#c9d9e6)}
.contact-line{position:absolute;left:544px;font-size:6.3px;color:#aaa;display:flex;gap:6px;line-height:8px}
.contact-line.phone{font-size:10px;color:#fff}
.bottom-bar{position:absolute;left:0;top:1175px;width:733px;height:25px;background:#111;font-size:6.3px;color:#888}
.copyright{position:absolute;left:115px;top:9px}
.follow{position:absolute;left:471px;top:4px;font-family:"Dancing Script",cursive;font-size:11px;color:#ddd}
.social{position:absolute;top:5px;width:15px;height:15px;border-radius:50%}
</style>
</head>
<body>

<header class="site-header">
  <div class="brand"><span class="brand-dot"></span><span class="brand-name">Vexlo</span></div>
  <nav class="main-nav">
    <div class="nav-item" style="width:41px"><svg width="9" height="10" viewBox="0 0 9 10"><circle cx="4.5" cy="3" r="2.5" fill="#ccc"/><path d="M0 10a4.5 4 0 0 1 9 0z" fill="#ccc"/></svg>About</div>
    <div class="nav-item" style="width:55px"><svg width="10" height="10" viewBox="0 0 10 10"><circle cx="4" cy="6" r="3" fill="#ccc"/><circle cx="8" cy="2" r="2" fill="#ccc"/></svg>Services</div>
    <div class="nav-item active" style="width:56px"><svg width="10" height="10" viewBox="0 0 10 10"><circle cx="5" cy="5" r="4.5" fill="#fff"/><circle cx="5" cy="5" r="1.6" fill="#262626"/></svg>Portfolio</div>
    <div class="nav-item" style="width:71px"><svg width="11" height="9" viewBox="0 0 11 9"><rect x=".5" y=".5" width="10" height="8" fill="none" stroke="#ccc"/><path d="M2 3h7M2 5h7" stroke="#ccc"/></svg>Short News</div>
    <div class="nav-item contact" style="width:51px"><svg width="9" height="10" viewBox="0 0 9 10"><rect width="9" height="10" rx="1" fill="#fff"/><path d="M3 3h3v4H3" fill="none" stroke="#5aa515"/></svg>Contact</div>
  </nav>
</header>

<section class="hero">
  <h1 class="hero-title">Welcome to Vexlo</h1>
  <p class="hero-lead">With Vexlo, Anyone Can Make a Professional Mobile Apps.</p>
  <div class="tag" style="left:114px"><svg width="10" height="10" viewBox="0 0 10 10"><circle cx="5" cy="5" r="4.3" fill="none" stroke="#2378ee"/><path d="M2.8 5.2l1.5 1.4 3-3" fill="none" stroke="#2378ee" stroke-width="1.2"/></svg>Mobile Apps</div>
  <div class="tag" style="left:240px"><svg width="10" height="10" viewBox="0 0 10 10"><circle cx="5" cy="5" r="4.3" fill="none" stroke="#2378ee"/><path d="M2.8 5.2l1.5 1.4 3-3" fill="none" stroke="#2378ee" stroke-width="1.2"/></svg>Mobile Games</div>
  <div class="cta">GET STARTED <span class="cta-dot"><svg width="10" height="10" viewBox="0 0 10 10"><path d="M5 1v6M2 5l3 3 3-3" fill="none" stroke="#4a9410" stroke-width="1.6"/></svg></span></div>
  <div class="tablet" role="img" aria-label="Tablet computer showing a mobile home screen with colourful app widgets"></div>
  <div class="slider-dots"><span></span><span class="on"></span><span></span></div>
</section>

<section class="services">
  <h2 class="section-title" style="top:313px">Our <span class="hl">Services</span></h2>
  <p class="intro" style="top:341px">Lorem Ipsum is simply dummy text of the printing and typesetting industry. Lorem Ipsum has been the industry's standard dummy text ever since the 1500s, when an unknown printer took a galley of type and scrambled it to make a type specimen book.</p>

  <div class="service" style="left:115px">
    <svg width="12" height="18" viewBox="0 0 12 18"><rect x="1" y="1" width="10" height="16" rx="1.5" fill="none" stroke="#444" stroke-width="1.6"/><path d="M1 13.5h10" stroke="#444" stroke-width="1.2"/><circle cx="6" cy="15.3" r=".9" fill="#444"/></svg>
    <h3>Mobile <span class="hl">Apps</span></h3>
    <p>Lorem Ipsum is simply dummy text of the printing and industry.</p>
  </div>
  <div class="service featured" style="left:244px">
    <svg width="20" height="17" viewBox="0 0 20 17"><rect x="1" y="1" width="18" height="12" rx="1" fill="none" stroke="#fff" stroke-width="1.8"/><path d="M7 16h6M10 13v3" stroke="#fff" stroke-width="1.8"/></svg>
    <h3>IT Consulting</h3>
    <p>Lorem Ipsum is simply dummy text of the printing and industry.</p>
  </div>
  <div class="service" style="left:374px">
    <svg width="18" height="16" viewBox="0 0 18 16"><rect x="1" y="1" width="16" height="14" fill="none" stroke="#444" stroke-width="1.5"/><path d="M1 4.5h16" stroke="#444" stroke-width="1.5"/></svg>
    <h3>Apps <span class="hl">Software</span></h3>
    <p>Lorem Ipsum is simply dummy text of the printing and industry.</p>
  </div>
  <div class="service" style="left:503px">
    <svg width="20" height="18" viewBox="0 0 20 18"><circle cx="7" cy="7" r="5" fill="none" stroke="#444" stroke-width="3" stroke-dasharray="2.5 1.5"/><circle cx="15" cy="14" r="3" fill="none" stroke="#444" stroke-width="2" stroke-dasharray="1.6 1"/></svg>
    <h3>Web <span class="hl">Development</span></h3>
    <p>Lorem Ipsum is simply dummy text of the printing and industry.</p>
  </div>
</section>

<section class="about">
  <h2 class="section-title">About Vexlo</h2>
  <div class="video">
    <div class="video-icon"><svg width="12" height="12" viewBox="0 0 12 12"><path d="M3 1l8 5-8 5z" fill="#d0d0d0"/></svg></div>
    Watch Our 1 Min Video
  </div>
  <h3 class="about-head">Computer Business Consultants</h3>
  <p class="about-sub">Lorem Ipsum is simply dummy text of the printing and typesetting industry.</p>
  <p class="about-text">Sed ut perspiciatis unde omnis iste natus error sit voluptatem accusantium doloremque laudantium, totam rem aperiam, eaque ipsa quae ab illo inventore veritatis et quasi architecto beatae vitae dicta sunt explicabo. Nemo enim ipsam voluptatem quia voluptas sit aspernatur aut odit aut fugit, sed quia consequuntur magni dolores eos qui ratione voluptatem sequi nesciunt. Neque porro quisquam est, qui dolorem ipsum quia dolor sit.</p>
  <div class="btn" style="left:325px;top:156px;width:67px">Read More <i></i></div>
</section>

<section class="portfolio">
  <h2 class="section-title" style="top:779px">Portfolio</h2>
  <p class="intro" style="top:812px">Lorem Ipsum is simply dummy text of the printing and typesetting industry. Lorem Ipsum has been the industry's standard dummy text ever since the 1500s, when an unknown printer took a galley of type and scrambled it to make a type specimen book.</p>

  <div class="work" style="left:117px">
    <div class="work-thumb" role="img" aria-label="Chat app screens on a smartphone" style="background:radial-gradient(circle,#f4f7f2,#cfe3c4)"></div>
    <h4>ChatLoop</h4><p>Lorem Ipsum is simply dummy text of the printing</p>
  </div>
  <div class="work" style="left:248px">
    <div class="work-thumb" role="img" aria-label="Mobile playground app artwork" style="background:linear-gradient(#fff,#f1f1f1)"></div>
    <h4>Mobzy</h4><p>Lorem Ipsum is simply dummy text of the printing</p>
  </div>
  <div class="work" style="left:379px">
    <div class="work-thumb" role="img" aria-label="Navigation app showing a road map" style="background:linear-gradient(160deg,#7c9a86,#4b6a3c 50%,#5a3a8c)">GPS MAP</div>
    <h4>Gps Map</h4><p>Lorem Ipsum is simply dummy text of the printing</p>
  </div>
  <div class="work" style="left:509px">
    <div class="work-thumb" role="img" aria-label="Colourful pet game artwork" style="background:linear-gradient(160deg,#7fc6f0,#f2c94c 55%,#8a4fb0)"></div>
    <h4>Tiny Critters</h4><p>Lorem Ipsum is simply dummy text of the printing</p>
  </div>

  <div class="btn" style="left:336px;top:1023px;width:62px">View All <i></i></div>
</section>

<footer class="site-footer">
  <h5 class="footer-h" style="left:115px">Site Map</h5>
  <ul class="sitemap"><li>Home</li><li>About</li><li>Services</li><li>Short News</li><li>Contact</li><li>Portfolio</li></ul>

  <h5 class="footer-h" style="left:183px">Recent News</h5>
  <svg class="abs" style="left:295px;top:20px" width="30" height="8" viewBox="0 0 30 8"><path d="M8 4H1M4 1L1 4l3 3M20 4h7M24 1l3 3-3 3" fill="none" stroke="#aaa"/></svg>
  <p class="news-item" style="top:35px">Lorem Ipsum is simply dummy text of the printing and typesetting industry. Lorem Ipsum has been the industry's standard.<em>5 Days ago</em></p>
  <p class="news-item" style="top:73px">Lorem Ipsum is simply dummy text of the printing and typesetting industry. Lorem Ipsum has been the industry's standard.<em>10 Days ago</em></p>

  <div class="map" role="img" aria-label="Street map of the office location"></div>

  <h5 class="footer-h" style="left:544px">Contact Us</h5>
  <div class="contact-line" style="top:34px"><svg width="7" height="9" viewBox="0 0 7 9"><path d="M3.5 9L.5 4a3 3 0 1 1 6 0z" fill="#888"/></svg><span style="padding-left:1px">1420 Harbor Lane 12<br>Bay City, CA 90000</span></div>
  <div class="contact-line phone" style="top:55px"><svg width="9" height="8" viewBox="0 0 9 8" style="margin-top:2px"><rect width="9" height="8" rx="1" fill="#bbb"/></svg>(555) 014-2290</div>
  <div class="contact-line" style="top:72px"><svg width="8" height="6" viewBox="0 0 8 6"><rect width="8" height="6" fill="#888"/><path d="M0 0l4 3 4-3" fill="none" stroke="#222"/></svg>info@vexlo.example</div>
  <div class="contact-line" style="top:83px"><span style="width:8px"></span>me@vexlo.example</div>
</footer>

<div class="bottom-bar">
  <p class="copyright">Copyright © 2013 Vexlo. All Rights Reserved.</p>
  <span class="follow">Follow Us On</span>
  <span class="social" style="left:537px;background:#3b5998"></span>
  <span class="social" style="left:559px;background:#2fa9e0"></span>
  <span class="social" style="left:581px;background:#1a6ea0"></span>
  <span class="social" style="left:603px;background:#d34836"></span>
</div>

</body>
</html>
```